Zielgruppe
Wir arbeiten in folgenden Bereichen:
- Mediation
- Konfliktmanagement
- Coaching
- Training
- Teamtraining
Über eine professionelle Webseite möchten wir neue Kunden gewinnen. Dazu möchten wir uns und unsere Leistungen vorstellen sowie dem Benutzer die Möglichkeit geben, sich über unsere anstehenden Projekte und Events zu informieren sowie uns zu kontaktieren.
Zielgruppe: Unsere Arbeit richtet sich an alle. Im Fokus stehen dabei Unternehmen. Theoretisch ist aber auch Arbeit mit Privatpersonen denkbar.
Aufgabenstellung
Farben: Dunkelblau, hellblau, weiß - Siehe Farben im PDF-Anhang. Eine weitere Akzentfarbe ist möglich.
Es geht ausschließlich um das Webdesign. Keine technische Umsetzung ist gewünscht.
Schriften: Bitte nur freie Schriften verwenden. Am besten wären Google Fonts.
Freie Stockfotos dürfen verwendet werden.
Das Design muss auf Desktop (optimiert auf ca. 1400px) und Mobile funktionieren (Responsive).
Nice to have wären optimierte App- und Favicons die auch vom Logo abweichen dürfen.
Die Seite wird mehrsprachig sein.
Für die Icons nur freie Icons verwenden.
Uns gefallen diese Seiten sehr gut. Es darf sich gern daran orientiert werden:
https://ufer-sieben.de/de/
https://bolmerhof.com
Wir wünschen uns ein komponentenbasiertes Design. Es soll uns möglich sein, die Komponenten frei zu kombinieren und neue Seiten zu kreieren. Als Vorgaben möchten wir gern die drei Seiten haben, die unten folgen.
Lieferung bitte in Figma. Das Resultat muss später in unseren Account übertragen werden können.

```html
<!DOCTYPE html>
<html lang="de">
<head>
<meta charset="utf-8">
<title>Brückenwerk – Mediation, Coaching, Teamtraining</title>
<link rel="stylesheet" href="https://fonts.googleapis.com/css2?family=Poppins:wght@400;500;600;700&display=swap">
<style>
:root{
  --navy:#0e1720;
  --blue:#3a8fc4;
  --blue-line:#2f86bf;
  --ink:#1d1d1d;
  --white:#ffffff;
  --panel-shadow:0 4px 14px rgba(0,0,0,.12);
}
*{box-sizing:border-box;margin:0;padding:0}
html,body{width:1200px;height:4965px;overflow:hidden}
body{position:relative;background:var(--white);font-family:'Poppins',sans-serif;color:var(--ink)}
.abs{position:absolute}

/* header */
.site-header{left:0;top:0;width:1200px;height:189px;background:var(--navy)}
.brand{left:0;width:1200px;display:flex;justify-content:center;align-items:center;gap:18px;color:var(--white);font-weight:600}
.brand .mark{width:22px;height:22px;background:var(--blue)}
.brand .name{font-size:50px;line-height:1}
.lang{right:14px;top:162px;color:#cfd6dc;font-size:12px}
.main-nav{left:0;top:189px;width:1200px;height:64px;background:var(--blue)}
.main-nav a{position:absolute;top:21px;color:var(--white);font-size:17px;text-decoration:none;text-transform:uppercase;font-weight:400}
.main-nav a.active{font-weight:600}

/* hero */
.photo{background:linear-gradient(135deg,#8a8a8a,#d6d6d6 45%,#4a4a4a)}
.hero{left:62px;top:290px;width:1068px;height:440px}
.arrow{top:475px;width:48px;height:72px}
.welcome{left:62px;top:768px;font-size:24px}
.welcome-rule{left:62px;top:812px;width:46px;height:3px;background:var(--blue)}

h1,h2,h3{font-weight:600;color:var(--blue)}
.hello{font-size:79px;line-height:1}
.sub{font-size:48px;line-height:1.55;font-weight:600;color:var(--blue)}
.copy{font-size:25px;line-height:37.5px;text-align:justify}
.more{left:62px;top:1488px;font-size:24px;color:var(--blue)}

/* service cards */
.card{background:var(--white);border-radius:12px;box-shadow:var(--panel-shadow)}
.card svg.icon{position:absolute;left:14px;top:12px}
.card h4{position:absolute;left:16px;top:146px;font-size:18px;font-weight:600;text-transform:uppercase}
.card ul{position:absolute;left:16px;top:190px;list-style:none;font-size:18px;line-height:33px}
.card li{display:flex;align-items:center;gap:8px}
.tick{display:inline-block;width:22px;height:22px;border-radius:4px;background:var(--ink);position:relative}
.tick::after{content:"";position:absolute;left:7px;top:3px;width:6px;height:11px;border:solid #fff;border-width:0 2.5px 2.5px 0;transform:rotate(45deg)}

/* about */
.about-copy{font-size:20px;line-height:29.3px;text-align:justify}
.offer-panel{left:35px;top:2172px;width:554px;height:598px;background:var(--white);box-shadow:var(--panel-shadow)}
.offer{left:0;width:554px}
.offer svg{position:absolute;left:42px;top:6px}
.offer h3{position:absolute;left:143px;top:0;font-size:31px;font-weight:500}
.offer p{position:absolute;left:143px;top:44px;font-size:20px;line-height:29px;width:330px}
.values{left:642px;list-style:none}
.values li{position:absolute;left:0;display:flex;align-items:center;gap:30px;font-size:26px;white-space:nowrap}
.big-tick{display:inline-block;width:50px;height:50px;border-radius:9px;background:var(--navy);position:relative}
.big-tick::after{content:"";position:absolute;left:17px;top:8px;width:13px;height:24px;border:solid #fff;border-width:0 4px 4px 0;transform:rotate(45deg)}

/* events */
.event-text{background:var(--white);box-shadow:var(--panel-shadow)}
.event-text h3{position:absolute;font-size:35px;font-weight:500}
.event-text p{position:absolute;font-size:19px;line-height:29.5px;text-align:justify}
.btn{position:absolute;background:var(--blue);color:var(--white);font-size:19px;text-align:center;border-radius:4px;line-height:37px;height:37px}

/* contact */
.field{left:70px;width:590px;border:3px solid var(--blue-line);border-radius:4px;color:var(--blue);font-size:33px;padding:0 14px;line-height:47px}
.check{left:70px;top:4414px;width:47px;height:42px;background:var(--blue);border-radius:5px}
.check::after{content:"";position:absolute;left:17px;top:7px;width:11px;height:20px;border:solid #fff;border-width:0 3.5px 3.5px 0;transform:rotate(45deg)}
.submit{left:70px;top:4488px;width:590px;height:57px;background:var(--blue);color:var(--white);font-size:35px;line-height:57px;text-align:center;border-radius:4px}

/* footer */
.site-footer{left:0;top:4644px;width:1200px;height:321px;background:var(--navy)}
.footer-links{left:0;top:4818px;width:1200px;text-align:center;list-style:none;color:var(--white);font-size:24px;line-height:37.5px}
</style>
</head>
<body>

<header class="site-header abs"></header>
<div class="brand abs" style="top:68px">
  <span class="mark"></span>
  <span class="name">Brückenwerk</span>
</div>
<div class="lang abs">DE ⌄</div>

<nav class="main-nav abs">
  <a href="#" style="left:154px">Mediation, Coaching, Teamtraining</a>
  <a href="#" style="left:574px">Über uns</a>
  <a href="#" style="left:714px">Projekte &amp; Events</a>
  <a href="#" class="active" style="left:952px">Kontakt</a>
</nav>

<div class="hero photo abs" role="img" aria-label="Schwarzweißfoto: zwei Hände beim Händedruck"></div>
<svg class="arrow abs" style="left:36px" viewBox="0 0 48 72"><polyline points="36,8 10,36 36,64" fill="none" stroke="#3a8fc4" stroke-width="9"/></svg>
<svg class="arrow abs" style="left:1106px" viewBox="0 0 48 72"><polyline points="12,8 38,36 12,64" fill="none" stroke="#3a8fc4" stroke-width="9"/></svg>

<p class="welcome abs">Wilkommen!</p>
<div class="welcome-rule abs"></div>

<section>
  <h1 class="hello abs" style="left:62px;top:880px">Hallo.</h1>
  <h2 class="sub abs" style="left:62px;top:967px;width:440px">Wir sind<br>Brückenwerk.</h2>
  <p class="copy abs" style="left:62px;top:1158px;width:382px">Lorem ipsum dolor sit amet, consectetur adipiscing elit. Nunc vulputate libero et velit interdum, ac aliquet odio mattis. Class aptent taciti sociosqu ad litora torquent per conubia nostra, per inceptos himenaeos.</p>
  <a class="more abs">Mehr Details →</a>

  <div class="card abs" style="left:541px;top:875px;width:279px;height:312px">
    <svg class="icon" width="90" height="90" viewBox="0 0 90 90" fill="none" stroke="#3a8fc4" stroke-width="3"><path d="M25 70V55c-10-6-12-22-2-32 9-9 25-8 32 2 8 10 5 22-2 30v15"/><path d="M45 28l-6 14h10l-6 14"/></svg>
    <h4>Mediation</h4>
    <ul><li><span class="tick"></span>Lorem Ipsum</li><li><span class="tick"></span>Dolor sit amet</li></ul>
  </div>
  <div class="card abs" style="left:848px;top:875px;width:280px;height:312px">
    <svg class="icon" width="90" height="90" viewBox="0 0 90 90" fill="none" stroke="#3a8fc4" stroke-width="3"><rect x="48" y="8" width="30" height="22"/><circle cx="22" cy="20" r="7"/><circle cx="15" cy="58" r="6"/><circle cx="40" cy="58" r="6"/><circle cx="65" cy="58" r="6"/><path d="M5 78c0-8 20-8 20 0M30 78c0-8 20-8 20 0M55 78c0-8 20-8 20 0"/></svg>
    <h4>Coaching</h4>
    <ul><li><span class="tick"></span>Lorem Ipsum</li><li><span class="tick"></span>Dolor sit amet</li></ul>
  </div>
  <div class="card abs" style="left:541px;top:1211px;width:279px;height:310px">
    <svg class="icon" width="90" height="90" viewBox="0 0 90 90" fill="none" stroke="#3a8fc4" stroke-width="3"><path d="M15 10v18M45 10v18M75 10v18M10 24l5 5 5-5M40 24l5 5 5-5M70 24l5 5 5-5"/><circle cx="30" cy="50" r="7"/><circle cx="60" cy="50" r="7"/><path d="M16 80c0-12 28-12 28 0M46 80c0-12 28-12 28 0"/></svg>
    <h4 style="top:152px">Teamtraining</h4>
    <ul style="top:196px"><li><span class="tick"></span>Lorem Ipsum</li><li><span class="tick"></span>Dolor sit amet</li></ul>
  </div>
  <div class="card abs" style="left:848px;top:1211px;width:280px;height:310px">
    <svg class="icon" width="90" height="90" viewBox="0 0 90 90" fill="none" stroke="#3a8fc4" stroke-width="3"><circle cx="45" cy="14" r="6"/><path d="M35 30h14v42M30 72h30"/></svg>
    <h4 style="top:152px">Information</h4>
    <ul style="top:196px"><li><span class="tick"></span>Lorem Ipsum</li><li><span class="tick"></span>Dolor sit amet</li></ul>
  </div>
</section>

<section>
  <div class="photo abs" style="left:35px;top:1633px;width:748px;height:470px;background:linear-gradient(90deg,#3a3a3a,#9a9a9a 45%,#e6e6e6 55%,#3a3a3a)" role="img" aria-label="Schwarzweißfoto: die beiden Mediatoren vor einem Flipchart an einer Ziegelwand"></div>
  <h2 class="hello abs" style="left:815px;top:1627px">Hallo.</h2>
  <h3 class="sub abs" style="left:815px;top:1714px">Das sind wir.</h3>
  <p class="about-copy abs" style="left:820px;top:1800px;width:330px">Lorem ipsum dolor sit amet, consectetur adipiscing elit. Nunc vulputate libero et velit interdum, ac aliquet odio mattis. Class aptent taciti sociosqu ad litora torquent per conubia nostra, per inceptos himenaeos. Class aptent taciti sociosqu ad litora torquent per conubia nostra, per inceptos himenaeos.</p>

  <div class="offer-panel abs"></div>
  <div class="offer abs" style="left:35px;top:2200px">
    <svg width="66" height="56" viewBox="0 0 66 56" fill="none" stroke="#3a8fc4" stroke-width="3"><circle cx="12" cy="8" r="6"/><path d="M4 22h20v8H4zM4 40h36v12H4z"/><circle cx="54" cy="28" r="6"/><path d="M44 52c0-10 20-10 20 0"/></svg>
    <h3>Mediation</h3>
    <p>Lorem ipsum dolor sit amet, consectetur adipiscing elit.</p>
  </div>
  <div class="offer abs" style="left:35px;top:2343px">
    <svg width="66" height="66" viewBox="0 0 66 66" fill="none" stroke="#3a8fc4" stroke-width="3"><rect x="18" y="4" width="44" height="30" rx="3"/><path d="M26 14h28M26 22h20"/><circle cx="14" cy="36" r="6"/><path d="M4 64V48h18l14-8"/></svg>
    <h3>Vorträge</h3>
    <p>Lorem ipsum dolor sit amet, consectetur adipiscing elit.</p>
  </div>
  <div class="offer abs" style="left:35px;top:2495px">
    <svg width="66" height="66" viewBox="0 0 66 66" fill="none" stroke="#3a8fc4" stroke-width="3"><rect x="24" y="4" width="18" height="34" rx="9"/><path d="M16 30c0 20 34 20 34 0M33 48v12"/></svg>
    <h3>Training</h3>
    <p>Lorem ipsum dolor sit amet, consectetur adipiscing elit.</p>
  </div>
  <div class="offer abs" style="left:35px;top:2642px">
    <svg width="66" height="66" viewBox="0 0 66 66" fill="none" stroke="#3a8fc4" stroke-width="3"><circle cx="33" cy="33" r="28"/><circle cx="33" cy="20" r="2.5" fill="#3a8fc4"/><path d="M28 28h6v20M27 48h14"/></svg>
    <h3>Beratung</h3>
    <p>Lorem ipsum dolor sit amet, consectetur adipiscing elit.</p>
  </div>

  <ul class="values abs" style="top:0">
    <li style="top:2169px"><span class="big-tick"></span>Verantwortungsbewusstsein</li>
    <li style="top:2267px"><span class="big-tick"></span>Seriösität</li>
    <li style="top:2367px"><span class="big-tick"></span>Engagement</li>
    <li style="top:2465px"><span class="big-tick"></span>Zielorientiert</li>
    <li style="top:2564px"><span class="big-tick"></span>Strategisch</li>
    <li style="top:2663px"><span class="big-tick"></span>Bildend</li>
  </ul>
</section>

<section>
  <h2 class="hello abs" style="left:57px;top:2891px">Hallo.</h2>
  <h3 class="sub abs" style="left:57px;top:2978px">Bock auf Events?</h3>

  <div class="event-text abs" style="left:70px;top:3068px;width:1071px;height:295px">
    <h3 style="left:25px;top:22px">Business Coaching</h3>
    <p style="left:25px;top:75px;width:432px">Lorem ipsum dolor sit amet, consectetur adipiscing elit. Nunc vulputate libero et velit interdum, ac aliquet odio mattis. Class aptent taciti sociosqu ad litora torquent per conubia nostra, per inceptos himenaeos.</p>
    <span class="btn" style="left:25px;top:238px;width:156px">Buchen</span>
  </div>
  <div class="photo abs" style="left:567px;top:3068px;width:574px;height:295px;background:linear-gradient(180deg,#2a2a2a,#7a7a7a 50%,#1c1c1c)" role="img" aria-label="Schwarzweißfoto: Vortrag vor Publikum mit Leinwand"></div>

  <div class="event-text abs" style="left:70px;top:3407px;width:1071px;height:297px">
    <h3 style="right:24px;top:18px">Private Coaching</h3>
    <p style="left:616px;top:77px;width:431px">Lorem ipsum dolor sit amet, consectetur adipiscing elit. Nunc vulputate libero et velit interdum, ac aliquet odio mattis. Class aptent taciti sociosqu ad litora torquent per conubia nostra, per inceptos himenaeos.</p>
    <span class="btn" style="left:890px;top:240px;width:157px">Buchen</span>
  </div>
  <div class="photo abs" style="left:70px;top:3407px;width:574px;height:297px;background:linear-gradient(90deg,#d8d8d8,#6a6a6a 45%,#efefef)" role="img" aria-label="Schwarzweißfoto: zwei Frauen im Gespräch vor einer Fensterfront"></div>
</section>

<section>
  <div class="field abs" style="top:3840px;height:53px">Name</div>
  <div class="field abs" style="top:3921px;height:53px">E-Mail Adresse</div>
  <div class="field abs" style="top:4003px;height:378px">Ihre Nachricht</div>
  <div class="check abs"></div>
  <p class="abs" style="left:136px;top:4416px;font-size:30px">Abboniere den Newsletter.</p>
  <div class="submit abs">Absenden</div>

  <h2 class="hello abs" style="right:70px;top:3825px">Hallo.</h2>
  <h3 class="sub abs" style="right:70px;top:3912px">Get Connected.</h3>
  <div class="photo abs" style="left:743px;top:3998px;width:387px;height:547px;background:linear-gradient(160deg,#e8e8e8,#bdbdbd 40%,#1a1a1a 70%,#9a9a9a)" role="img" aria-label="Schwarzweißfoto: Tastatur und Tablet mit Stift"></div>
</section>

<footer class="site-footer abs"></footer>
<div class="brand abs" style="top:4730px">
  <span class="mark" style="width:18px;height:18px"></span>
  <span class="name" style="font-size:40px">Brückenwerk</span>
</div>
<ul class="footer-links abs">
  <li>Impressum</li>
  <li>Datenschutz</li>
  <li>Kontakt</li>
</ul>

</body>
</html>
```